Donation for lead promotion

I am looking for a banner that can be placed on our emails, quotationion forms and invoices.
This is direct to existing clients and new, we are offering a charity donation for any genuine sales lead enquiry an existing customer gives us, this cannot be them but a contact they may have or friend etc etc. I want a fun/cartoon style graphic with the slogan
"A donation for a lead" being incorporated in the design.
It should be colourful, bold and in directed at B2B.
We would want a full edit version high res pdf so we can adjust to fit on various stationery etc.

The charity at the moment is bright acorn fund and hope to have another charity on board as well.

Target Market(s)

business to business

Industry/Entity Type

Charity

Requirements
Must have
• charity logo do be visiual on the charity tubs
Nice to have
• the collection boxes are to give you an idea, please find a suitable high res pdf image you can use.
charity collection boxes websites have several images to give you the idea

```html
<!DOCTYPE html>
<html lang="en">
<head>
<meta charset="utf-8">
<title>A donation for a lead</title>
<link rel="stylesheet" href="https://fonts.googleapis.com/css2?family=Anton&family=Nunito:wght@700&display=swap">
<style>
  :root {
    --sky-deep: #0d3a9c;
    --sky-mid: #1f5fd0;
    --sky-glow: #5fa6f2;
    --ground: #ffffff;
    --ground-shade: #e4e6ec;
    --title: #ffffff;
    --title-shadow: rgba(5, 25, 80, 0.55);
    --tin-yellow: #f4e500;
    --tin-yellow-dark: #c9b800;
    --tin-pink: #ee1c8c;
    --tin-pink-dark: #b8106a;
    --label: #ffffff;
    --care-blue: #1d5fa8;
    --care-gold: #f3c21a;
    --acorn-ink: #5a2d82;
    --labels-ink: #7a1f3d;
  }
  * { margin: 0; padding: 0; box-sizing: border-box; }
  html, body { width: 1200px; height: 900px; overflow: hidden; }
  .banner {
    position: relative;
    width: 1200px;
    height: 900px;
    overflow: hidden;
    background: radial-gradient(ellipse 70% 60% at 62% 18%, var(--sky-glow) 0%, var(--sky-mid) 40%, var(--sky-deep) 100%);
  }
  .ground { position: absolute; left: 0; bottom: 0; width: 1200px; height: 300px; }
  .slogan {
    position: absolute;
    left: 168px;
    top: 290px;
    width: 800px;
    text-align: center;
    font-family: "Anton", sans-serif;
    font-size: 92px;
    line-height: 1;
    letter-spacing: 1px;
    color: var(--title);
    text-shadow: 0 5px 8px var(--title-shadow);
  }
  .tin {
    position: absolute;
    top: 495px;
    border-radius: 14px 14px 22px 22px;
  }
  .tin--care { left: 158px; width: 247px; height: 345px;
    background: linear-gradient(90deg, var(--tin-yellow-dark), var(--tin-yellow) 30%, var(--tin-yellow) 70%, var(--tin-yellow-dark)); }
  .tin--acorn { left: 458px; width: 247px; height: 367px;
    background: linear-gradient(90deg, var(--tin-pink-dark), var(--tin-pink) 30%, var(--tin-pink) 70%, var(--tin-pink-dark)); }
  .tin--labels { left: 745px; width: 257px; height: 345px;
    background: linear-gradient(90deg, var(--tin-yellow-dark), var(--tin-yellow) 30%, var(--tin-yellow) 70%, var(--tin-yellow) 70%, var(--tin-yellow-dark)); }
  .tin-label {
    position: absolute;
    top: 577px;
    background: var(--label);
    border-radius: 14px;
    display: flex;
    flex-direction: column;
    align-items: center;
    justify-content: center;
    text-align: center;
    font-family: "Nunito", sans-serif;
    font-weight: 700;
    padding: 12px;
  }
  .tin-label--care { left: 180px; width: 203px; height: 203px; gap: 14px; }
  .tin-label--acorn { left: 495px; width: 173px; height: 215px; gap: 14px; }
  .tin-label--labels { left: 780px; width: 195px; height: 203px; gap: 4px; }
  .care-intro { color: var(--care-blue); font-size: 19px; }
  .care-name-row { display: flex; align-items: center; gap: 10px; }
  .care-name { color: var(--care-blue); font-size: 22px; line-height: 1.15; }
  .care-mark { width: 30px; height: 30px; border-radius: 50%; background: var(--care-gold); flex: none; }
  .acorn-name { color: var(--acorn-ink); font-size: 27px; line-height: 1.1; }
  .acorn-art { width: 140px; height: 90px; border-radius: 10px;
    background: linear-gradient(180deg, #f7d9a8, #9fd07a); }
  .labels-name { color: var(--labels-ink); font-size: 24px; }
  .labels-tag { color: var(--labels-ink); font-size: 12px; }
</style>
</head>
<body>
<main class="banner">
  <svg class="ground" viewBox="0 0 1200 300" aria-hidden="true">
    <path d="M0 110 C 200 60, 380 170, 620 160 S 1000 90, 1200 150 L1200 300 L0 300 Z" fill="var(--ground)"/>
    <path d="M0 230 C 300 180, 700 200, 1200 250 L1200 300 L0 300 Z" fill="var(--ground-shade)"/>
  </svg>

  <h1 class="slogan">A donation for a lead</h1>

  <div class="tin tin--care" role="img" aria-label="Yellow charity collection tin with wire handle"></div>
  <div class="tin tin--acorn" role="img" aria-label="Pink charity collection tin with wire handle"></div>
  <div class="tin tin--labels" role="img" aria-label="Yellow charity collection tin with wire handle"></div>

  <div class="tin-label tin-label--care">
    <p class="care-intro">Raising funds in aid of</p>
    <div class="care-name-row">
      <p class="care-name">Silver Lantern Care</p>
      <span class="care-mark"></span>
    </div>
  </div>

  <div class="tin-label tin-label--acorn">
    <p class="acorn-name">bright acorn fund</p>
    <div class="acorn-art" role="img" aria-label="Cartoon of a group of happy children"></div>
  </div>

  <div class="tin-label tin-label--labels">
    <p class="labels-name">Northgate Labels</p>
    <p class="labels-tag">labels made simply</p>
  </div>
</main>
</body>
</html>
```